Yard signs to bring awareness to the neighborhood we are here to help you also.

My project is to build brand awareness in a Neighborhood before during and after my company's get a home owner approve from there in insurance Approved to replace there roof due to the recent storms. Call us we can do the same for you.
We are trying to let the neighborhood know that they may also have enough storm damage for them to have there roof and gutters replace at no cost to them. And we can help with there claim to go over all the steps involved.

Target Market(s)

Brand awareness to Home owner in the neighborhood

Industry/Entity Type

Roofing

Font styles to use
Sans Serif

Requirements
Must have
• Insurance Approved
Wind & Hail
Call For Free consultation
512 846-2971
Nice to have
• Make phone # big and bold

```html
<!DOCTYPE html>
<html lang="en">
<head>
<meta charset="utf-8">
<title>R&amp;R Roofing LLC. – Yard Sign</title>
<link rel="stylesheet" href="https://fonts.googleapis.com/css2?family=Bebas+Neue&amp;family=La+Belle+Aurore&amp;family=Montserrat:wght@500;600;800;900&amp;display=swap">
<style>
  :root {
    --page-bg: #e4e4e6;
    --sign-dark: #1b1c29;
    --sign-darker: #12131c;
    --mint: #7ffbe0;
    --teal: #2fd3ad;
    --navy: #234a93;
    --white: #ffffff;
    --black: #000000;
  }
  * { margin: 0; padding: 0; box-sizing: border-box; }
  html, body {
    width: 1200px; height: 1200px; overflow: hidden;
    background: var(--page-bg);
  }
  .yard-sign {
    position: absolute; left: 42px; top: 228px;
    width: 1116px; height: 744px;
    background: var(--sign-dark);
    overflow: hidden;
  }
  .house-photo {
    position: absolute; left: 0; top: 0; width: 100%; height: 471px;
    background: radial-gradient(ellipse at 50% 60%, #2e3040 0%, #202231 55%, #15161f 100%);
  }
  .company-name {
    position: absolute; left: 40px; top: 40px; width: 100%;
    text-align: center;
    font-family: "Bebas Neue", sans-serif; font-weight: 400;
    font-size: 112px; line-height: 1;
    color: var(--mint);
    letter-spacing: 5px;
  }
  .brand-mark {
    position: absolute; left: 186px; top: 160px;
    width: 115px; height: 168px;
    display: flex; flex-direction: column; align-items: center; justify-content: center; gap: 10px;
  }
  .brand-mark .dot {
    width: 84px; height: 84px; border-radius: 50%;
    background: var(--teal);
  }
  .brand-mark .mark-name {
    font-family: "Bebas Neue", sans-serif;
    font-size: 44px; line-height: 1; color: var(--teal);
  }
  .tagline {
    font-family: "La Belle Aurore", cursive;
    color: var(--teal);
    font-size: 46px; line-height: 1; white-space: nowrap;
  }
  .tagline .line-one { position: absolute; left: 309px; top: 212px; }
  .tagline .line-two { position: absolute; left: 393px; top: 272px; }
  .storm-types {
    position: absolute; left: 0; top: 346px; width: 100%;
    text-align: center;
    font-family: "Montserrat", sans-serif; font-weight: 600;
    font-size: 24px; line-height: 1; letter-spacing: 6px;
    color: var(--mint);
  }
  .services {
    position: absolute; left: 0; top: 394px; width: 100%;
    display: flex; justify-content: center; align-items: center; gap: 30px;
    font-family: "Montserrat", sans-serif; font-weight: 600;
    font-size: 55px; line-height: 1; color: var(--white);
  }
  .services .divider {
    width: 30px; height: 42px; background: var(--teal);
  }
  .contact-band {
    position: absolute; left: 0; top: 471px; width: 100%; height: 172px;
    background: var(--mint);
  }
  .phone-row {
    position: absolute; left: 87px; top: -4px;
    display: flex; align-items: center; gap: 10px;
  }
  .phone-icon { width: 86px; height: 86px; }
  .phone-number {
    font-family: "Montserrat", sans-serif; font-weight: 800;
    font-size: 130px; line-height: 1; color: var(--navy);
    letter-spacing: -2px;
  }
  .call-to-action {
    position: absolute; left: 0; top: 113px; width: 100%;
    text-align: center;
    font-family: "Montserrat", sans-serif; font-weight: 900;
    font-size: 51px; line-height: 1; color: var(--black);
    letter-spacing: 1px;
  }
  .insurance-band {
    position: absolute; left: 0; top: 643px; width: 100%; height: 101px;
    background: var(--sign-darker);
    display: flex; align-items: center; justify-content: center;
    font-family: "Montserrat", sans-serif; font-weight: 600;
    font-size: 58px; color: var(--white);
    letter-spacing: 1px;
  }
</style>
</head>
<body>
  <div class="yard-sign">
    <div class="house-photo" role="img" aria-label="Darkened photo of a two-storey house with a storm-damaged shingle roof, trees behind"></div>

    <h1 class="company-name">R&amp;R Roofing LLC.</h1>

    <div class="brand-mark">
      <span class="dot"></span>
      <span class="mark-name">R&amp;R</span>
    </div>

    <p class="tagline">
      <span class="line-one">Nobody Does it Better!</span>
      <span class="line-two">Here To Serve.</span>
    </p>

    <p class="storm-types">WIND &amp; HAIL</p>

    <div class="services">
      <span>ROOFING</span>
      <span class="divider"></span>
      <span>SIDING</span>
      <span class="divider"></span>
      <span>GUTTERS</span>
    </div>

    <div class="contact-band">
      <div class="phone-row">
        <svg class="phone-icon" viewBox="0 0 88 88" aria-hidden="true">
          <circle cx="44" cy="44" r="41" fill="none" stroke="#234a93" stroke-width="4"/>
          <path d="M28 24c3-2 6-2 8 1l5 8c1 2 1 4-1 6l-3 3c2 5 6 9 11 11l3-3c2-2 4-2 6-1l8 5c3 2 3 5 1 8l-3 3c-4 3-10 3-17-1-9-5-17-13-21-22-3-7-3-12 1-16z" fill="#234a93"/>
          <path d="M47 30a11 11 0 0 1 11 11M48 22a19 19 0 0 1 18 18M49 14a27 27 0 0 1 25 25" fill="none" stroke="#234a93" stroke-width="3.5" stroke-linecap="round"/>
        </svg>
        <span class="phone-number">512 846-2971</span>
      </div>
      <p class="call-to-action">CALL FOR FREE CONSULTATION</p>
    </div>

    <div class="insurance-band">INSURANCE APPROVED</div>
  </div>
</body>
</html>
```